Marlow Creek Stud website

We would like to create a horse stud/agistment farm website similar to this websites we have attached below:
www.hollistead.com.au
www.quandrell.com.au
www.barrowick.com
www.fenshaw.com.au
The main colour scheme are purple and white to align with the stable's racing colours.
We have also attach the company logo and also images of the farm and create some ideas for the website.
Many thanks for looking into this project!

```html
<!DOCTYPE html>
<html lang="en">
<head>
<meta charset="utf-8">
<title>Marlow Creek Stud</title>
<link rel="stylesheet" href="https://fonts.googleapis.com/css2?family=Michroma&family=Roboto:wght@400;500;700&display=swap">
<style>
:root{
  --purple:#3d1a47;
  --purple-dark:#2f1238;
  --purple-line:#54305e;
  --white:#ffffff;
  --ink:#222222;
  --muted:#8a8a8a;
  --soft:#eeeeee;
  --grass:#5c7a3a;
  --grass-dark:#34502a;
  --sky:#7fa7d8;
}
*{box-sizing:border-box;margin:0;padding:0}
html,body{width:1200px;height:2609px;overflow:hidden}
body{font-family:"Roboto",Arial,sans-serif;color:var(--ink);background:var(--white);position:relative}
.display{font-family:"Michroma","Arial Black",sans-serif;font-weight:400}
a{color:inherit;text-decoration:none}

/* header */
.site-header{position:absolute;top:0;left:0;width:1200px;height:75px;background:var(--purple);display:flex;align-items:center;padding:0 162px}
.brand{color:var(--white);font-size:15px;font-weight:500;letter-spacing:1px;display:flex;align-items:center;gap:8px}
.brand-dot{width:12px;height:12px;border-radius:50%;background:var(--white)}
.main-nav{margin-left:auto;display:flex;gap:24px;font-size:11px;color:var(--white)}
.main-nav a{position:relative}
.main-nav a.active::before{content:"";position:absolute;left:0;right:0;top:-27px;height:3px;background:var(--white)}
.social{display:flex;gap:6px;margin-left:22px}
.social span{width:11px;height:11px;background:#b9a9bf;border-radius:2px}
.social span:first-child{background:var(--white)}

/* hero */
.hero{position:absolute;top:75px;left:0;width:1200px;height:525px;background:linear-gradient(160deg,#6f8a55 0%,#4f6b35 35%,#7a7f5a 55%,#3f5a2c 80%,#2f4622 100%)}
.hero-inner{position:absolute;left:0;right:0;top:235px;text-align:center;color:var(--white)}
.hero-title{font-size:36px;letter-spacing:1px}
.hero-pill{display:inline-block;margin-top:8px;background:var(--white);color:var(--purple);font-size:15px;letter-spacing:3px;padding:4px 26px;border-radius:14px}
.hero-since{margin-top:12px;font-size:10px;letter-spacing:4px;display:flex;justify-content:center;align-items:center;gap:10px}
.hero-since i{display:block;width:50px;height:1px;background:var(--white)}
.hero-arrow{position:absolute;top:243px;width:38px;height:38px;border:2px solid var(--white);border-radius:50%}
.hero-arrow.prev{left:30px}.hero-arrow.next{right:30px}
.hero-dots{position:absolute;bottom:30px;left:0;right:0;display:flex;justify-content:center;gap:8px}
.hero-dots span{width:20px;height:5px;border-radius:3px;background:rgba(255,255,255,.45)}
.hero-dots span:first-child{background:var(--white)}

.section-title{text-align:center;font-size:22px;letter-spacing:11px;color:var(--ink)}

/* stallions */
.stallions{position:absolute;top:600px;left:0;width:1200px;height:447px}
.stallions .section-title{margin-top:54px}
.stallion-panel{position:absolute;top:122px;left:162px;width:876px;height:264px;background:var(--purple);display:flex;gap:22px;padding:22px 22px 0}
.stallion-card{width:192px;text-align:center;color:var(--white)}
.stallion-photo{height:200px;border:2px solid #d9d0dc}
.p1{background:linear-gradient(180deg,#6a8fc4,#a88a4a)}
.p2{background:linear-gradient(180deg,#4f86d0,#b9cbe0 60%,#7c8e4c)}
.p3{background:linear-gradient(180deg,#8c8d86,#6a8a45)}
.p4{background:linear-gradient(180deg,#6d7d86,#4e7d38)}
.stallion-name{font-size:12px;letter-spacing:1px;margin-top:9px}
.panel-arrow{position:absolute;top:105px;color:var(--white);font-size:18px;opacity:.7}

/* news */
.news{position:absolute;top:1047px;left:0;width:1200px;height:506px;background:linear-gradient(180deg,#e9ece9 0%,#dfe3dc 55%,#b9c4ac 100%)}
.news .section-title{margin-top:50px}
.news-grid{position:absolute;top:123px;left:162px;display:flex;gap:22px}
.news-card{width:428px;height:244px;background:var(--white);display:flex;box-shadow:0 2px 8px rgba(0,0,0,.08)}
.news-media{width:202px;position:relative}
.n1{background:linear-gradient(180deg,#6f9a4a,#8a6a45)}
.n2{background:linear-gradient(180deg,#8a8a7a,#6a4a30)}
.news-meta{position:absolute;left:0;right:0;bottom:0;height:50px;background:var(--purple);color:var(--white);padding:6px 16px}
.news-date{font-size:15px;font-weight:700}
.news-tag{font-size:11px;margin-top:2px}
.news-body{width:226px;padding:20px 22px}
.news-body h3{font-size:14px;font-weight:700;line-height:1.35}
.news-body p{font-size:10.5px;color:var(--muted);line-height:1.8;margin-top:14px}
.read-more{display:block;margin-top:16px;font-size:11px;font-weight:700;color:var(--purple)}
.see-all{position:absolute;top:420px;left:550px;width:100px;height:28px;border:1.5px solid var(--ink);border-radius:14px;font-size:10px;font-weight:700;display:flex;align-items:center;justify-content:center;gap:4px}

/* farm */
.farm{position:absolute;top:1553px;left:0;width:1200px;height:363px}
.farm-copy{position:absolute;left:162px;top:58px;width:430px}
.farm-copy h2{font-size:22px;letter-spacing:11px}
.farm-copy p{font-size:10.5px;color:var(--muted);line-height:1.9;margin-top:20px}
.farm-copy p+p{margin-top:12px}
.farm-link{display:block;margin-top:16px;font-size:10.5px;font-weight:700;color:var(--ink)}
.video{position:absolute;left:663px;top:61px;width:375px;height:242px;background:linear-gradient(180deg,#3a3a3a 0%,#6c6a60 35%,#5e8a3a 80%,#4b7a2e 100%)}
.video-title{position:absolute;top:12px;left:12px;color:var(--white);font-size:11px;display:flex;align-items:center;gap:6px}
.video-title span{width:12px;height:12px;border-radius:50%;background:var(--white)}
.video-play{position:absolute;left:166px;top:100px}

/* gallery */
.gallery{position:absolute;top:1916px;left:0;width:1200px;height:240px;display:flex}
.gallery div{flex:1}
.g1{background:linear-gradient(180deg,#5a3a6a,#3d2a40);position:relative}
.g1 svg{position:absolute;left:100px;top:100px}
.g2{background:linear-gradient(180deg,#c7ccd0,#6f8a3f)}
.g3{background:linear-gradient(180deg,#2f4a5a,#6f9a3a)}
.g4{background:linear-gradient(180deg,#7a9a5a,#4f8a3a)}
.g5{background:linear-gradient(180deg,#7a8a9a,#6a5a3a)}

/* footer */
.site-footer{position:absolute;top:2156px;left:0;width:1200px;height:401px;background:var(--purple)}
.signup{position:absolute;top:61px;left:162px;width:876px;height:92px;background:var(--white);border-radius:6px;padding:18px 21px}
.signup h2{font-size:24px;letter-spacing:2px;color:var(--purple)}
.signup p{font-size:12px;color:var(--muted);margin-top:4px}
.signup-form{position:absolute;right:24px;top:32px;display:flex}
.signup-form span{width:226px;height:30px;background:var(--soft);font-size:10px;color:var(--muted);padding:9px 10px}
.signup-form b{width:60px;height:30px;background:var(--purple);color:var(--white);font-size:10px;font-weight:500;display:flex;align-items:center;justify-content:center}
.footer-brand{position:absolute;left:170px;top:193px;color:var(--white);font-size:15px;font-weight:500;display:flex;align-items:center;gap:8px}
.footer-col{position:absolute;top:198px;color:var(--white)}
.footer-col h4{font-family:"Michroma",sans-serif;font-weight:400;font-size:11px;letter-spacing:.5px;margin-bottom:12px}
.footer-col p,.footer-col li{font-size:10.5px;line-height:1.75;color:#e6dde9;list-style:none}
.footer-col strong{font-weight:700;color:var(--white)}
.col-contact{left:386px}.col-links{left:610px}.col-stallions{left:836px}
.footer-social{display:flex;gap:8px;margin-top:8px}
.footer-social span{width:14px;height:14px;background:#b9a9bf;border-radius:2px}
.footer-social span:first-child{background:var(--white)}
.bottom-bar{position:absolute;top:2557px;left:0;width:1200px;height:52px;background:var(--purple);border-top:1px solid var(--purple-line);color:#e6dde9;font-size:10px;padding:20px 162px}
</style>
</head>
<body>

<header class="site-header">
  <div class="brand"><span class="brand-dot"></span>Marlow Creek</div>
  <nav class="main-nav">
    <a class="active" href="#">HOME</a><a href="#">OUR FARM</a><a href="#">STALLIONS</a><a href="#">SALES</a><a href="#">NEWS</a><a href="#">CONTACT</a>
  </nav>
  <div class="social"><span></span><span></span><span></span><span></span></div>
</header>

<section class="hero" role="img" aria-label="Aerial photograph of the farm with paddocks, stables and a round yard">
  <div class="hero-inner">
    <div class="hero-title display">MARLOW CREEK</div>
    <div class="hero-pill display">STUD | AGISTMENT FARM</div>
    <div class="hero-since display"><i></i>SINCE 1977<i></i></div>
  </div>
  <svg class="hero-arrow prev" viewBox="0 0 38 38"><path d="M21 13l-6 6 6 6" fill="none" stroke="#fff" stroke-width="2"/></svg>
  <svg class="hero-arrow next" viewBox="0 0 38 38"><path d="M17 13l6 6-6 6" fill="none" stroke="#fff" stroke-width="2"/></svg>
  <div class="hero-dots"><span></span><span></span><span></span></div>
</section>

<section class="stallions">
  <h2 class="section-title display">STALLIONS</h2>
  <div class="stallion-panel">
    <span class="panel-arrow" style="left:30px">&lsaquo;</span>
    <div class="stallion-card"><div class="stallion-photo p1" role="img" aria-label="Bay stallion standing in a golden field"></div><div class="stallion-name display">STALLIONS TITLE</div></div>
    <div class="stallion-card"><div class="stallion-photo p2" role="img" aria-label="Chestnut stallion under a blue sky"></div><div class="stallion-name display">STALLIONS TITLE</div></div>
    <div class="stallion-card"><div class="stallion-photo p3" role="img" aria-label="Chestnut horses grazing in a paddock"></div><div class="stallion-name display">STALLIONS TITLE</div></div>
    <div class="stallion-card"><div class="stallion-photo p4" role="img" aria-label="Palomino stallion on green grass"></div><div class="stallion-name display">STALLIONS TITLE</div></div>
    <span class="panel-arrow" style="right:30px">&rsaquo;</span>
  </div>
</section>

<section class="news" role="region" aria-label="Latest news over a faded racetrack background">
  <h2 class="section-title display">LATEST NEWS</h2>
  <div class="news-grid">
    <article class="news-card">
      <div class="news-media n1" role="img" aria-label="Rider jumping a horse over a fence">
        <div class="news-meta"><div class="news-date">06/01/2019</div><div class="news-tag">Stallion: Silverline</div></div>
      </div>
      <div class="news-body">
        <h3>Neque porro quisquam est, qui dolorem ipsum quia dolor sit amet</h3>
        <p>Nemo enim ipsam voluptatem quia voluptas sit aspernatur aut odit aut fugit, sed quia consequuntur magni dolores eos qui ratione voluptatem sequi nesciunt.</p>
        <a class="read-more" href="#">&rsaquo; Read More</a>
      </div>
    </article>
    <article class="news-card">
      <div class="news-media n2" role="img" aria-label="Bay horse in a halter">
        <div class="news-meta"><div class="news-date">06/01/2019</div><div class="news-tag">Stallion: Silverline</div></div>
      </div>
      <div class="news-body">
        <h3>Neque porro quisquam est, qui dolorem ipsum quia dolor sit amet</h3>
        <p>Nemo enim ipsam voluptatem quia voluptas sit aspernatur aut odit aut fugit, sed quia consequuntur magni dolores eos qui ratione voluptatem sequi nesciunt.</p>
        <a class="read-more" href="#">&rsaquo; Read More</a>
      </div>
    </article>
  </div>
  <a class="see-all" href="#">SEE ALL <svg width="12" height="8" viewBox="0 0 12 8"><path d="M0 4h10M7 1l3 3-3 3" fill="none" stroke="#222" stroke-width="1.3"/></svg></a>
</section>

<section class="farm">
  <div class="farm-copy">
    <h2 class="display">OUR FARM</h2>
    <p>Sed ut perspiciatis unde omnis iste natus error sit voluptatem accusantium doloremque laudantium, totam rem aperiam, eaque ipsa quae ab illo inventore veritatis et quasi architecto beatae vitae dicta sunt explicabo. Nemo enim ipsam voluptatem quia voluptas sit aspernatur aut odit aut fugit, sed quia consequuntur magni dolores eos qui ratione voluptatem sequi nesciunt. Neque porro quisquam est, qui dolorem ipsum quia dolor sit amet.</p>
    <p>Ut enim ad minima veniam, quis nostrum exercitationem ullam corporis suscipit laboriosam, nisi ut aliquid ex ea commodi consequatur. Quis autem vel eum iure reprehenderit qui in ea voluptate velit esse quam nihil molestiae consequatur.</p>
    <a class="farm-link" href="#">Learn More About Marlow Creek &rarr;</a>
  </div>
  <div class="video" role="img" aria-label="Video still of a grey racehorse and jockey galloping past flower beds">
    <div class="video-title"><span></span>Nemo enim ipsam voluptatem quia voluptas</div>
    <svg class="video-play" width="44" height="44" viewBox="0 0 44 44"><circle cx="22" cy="22" r="21" fill="rgba(0,0,0,.55)"/><path d="M17 13l14 9-14 9z" fill="#fff"/></svg>
  </div>
</section>

<section class="gallery">
  <div class="g1" role="img" aria-label="Group of horses at dusk"><svg width="38" height="38" viewBox="0 0 38 38"><circle cx="19" cy="19" r="17" fill="none" stroke="#fff" stroke-width="1.5"/><path d="M19 12v14M12 19h14" stroke="#fff" stroke-width="1.5"/></svg></div>
  <div class="g2" role="img" aria-label="Horses grazing under trees"></div>
  <div class="g3" role="img" aria-label="Palomino horse in a green paddock"></div>
  <div class="g4" role="img" aria-label="Aerial view of paddocks and shelters"></div>
  <div class="g5" role="img" aria-label="Timber fence under a cloudy sky"></div>
</section>

<footer class="site-footer">
  <div class="signup">
    <h2 class="display">SIGN UP</h2>
    <p>Be the first to discover our latest news &amp; stallion updates</p>
    <div class="signup-form"><span>Email address</span><b>Sign Up</b></div>
  </div>
  <div class="footer-brand"><span class="brand-dot"></span>Marlow Creek</div>
  <div class="footer-col col-contact">
    <h4>GET IN TOUCH</h4>
    <p>1059 Minima Rd,<br>nostrum 45 exer 100265</p>
    <p><strong>Email:</strong> info@marlowcreek.com</p>
    <p><strong>Phone:</strong> +123-4567-890<br><strong>Fax:</strong> +231-4567-890</p>
    <div class="footer-social"><span></span><span></span><span></span><span></span></div>
  </div>
  <div class="footer-col col-links">
    <h4>QUICK LINKS</h4>
    <ul><li>Home</li><li>Our Farm</li><li>Stallions</li><li>Sales</li><li>News</li><li>Contact</li></ul>
  </div>
  <div class="footer-col col-stallions">
    <h4>STALLIONS</h4>
    <ul><li>Harbour Prince</li><li>Night Turn</li><li>Stillwater</li><li>Always Ready</li><li>Brisk</li><li>Bold Statement</li><li>Iron Resolve</li></ul>
  </div>
</footer>
<div class="bottom-bar">&copy; Marlow Creek. | All rights reserved.</div>

</body>
</html>
```